Motor Vault Website - Part of the Brantley Group

A complimentary website is required for the launch of a 'Motor Vault' - a new service launched by industry renowned BRANTLEY. Motor Vault is an industry-first brand that designs and builds unique subterranean car parks for private residential homes in London and the influential counties within the UK. Please see here the direction of a new BRANTLEY Website - we would like Motor Vault to be complimentary and sit alongside BRANTLEY harmoniously - https://www.brantleyhq.example/brantley-nu-staging Brantley have some images, but whilst more professional images are in production - we have also attached pixmoor photos- named clearly as pixmoor. **Attached files include JPEG, .eps of logo and Brantley library images and Pixmoor Library Images - two versions of logo dependent on background colour. - Website needs to be sleek, chic and masculine.- Colour Palette - Grey/ Black/ White - Same visiual journey as Brantley website- Required areas within the sit include - About Us / Our Work / Contact Page

Target Market(s)

Luxury
Men

Number of Pages Required

2 page

Font styles to use
Sans Serif

Colors
e8e8e8
757575
1b1b1b
000000
9d9d9d
cbcbcb
f5f5f5

Requirements
Must have
• Complimentary of this site - https://www.brantleyhq.example/brantley-nu-staging
Should not have
• Colour

```html
<!DOCTYPE html>
<html lang="en">
<head>
<meta charset="utf-8">
<title>Motor Vault — Part of the Brantley Group</title>
<link rel="stylesheet" href="https://fonts.googleapis.com/css2?family=Work+Sans:wght@400;500;600;700&family=Noto+Serif:wght@400&display=swap">
<style>
:root{
  --white:#ffffff;
  --paper:#f5f5f5;
  --mist:#e8e8e8;
  --silver:#cbcbcb;
  --ash:#9d9d9d;
  --slate:#757575;
  --coal:#1b1b1b;
  --black:#000000;
  --sans:'Work Sans', Arial, sans-serif;
  --serif:'Noto Serif', Georgia, serif;
}
*{box-sizing:border-box;margin:0;padding:0}
html,body{width:1200px;height:2557px;overflow:hidden}
body{position:relative;background:var(--white);font-family:var(--sans);color:var(--coal)}
.abs{position:absolute}

/* header */
.site-header{left:0;top:0;width:1200px;height:82px;background:var(--white)}
.brand{display:flex;align-items:center;gap:8px;font-family:var(--sans);font-weight:600;color:var(--coal);letter-spacing:1px;white-space:nowrap}
.brand-mark{width:20px;height:20px;background:currentColor}
.site-header .brand{position:absolute;left:162px;top:24px;font-size:26px}
.brand-sub{position:absolute;font-size:7px;letter-spacing:.5px;color:var(--slate);white-space:nowrap}
.site-header .brand-sub{left:253px;top:56px}
.main-nav{position:absolute;top:33px;left:0;width:1200px;font-size:11px;letter-spacing:.4px;text-transform:uppercase}
.main-nav a{position:absolute;color:var(--coal);text-decoration:none}
.main-nav .active{font-weight:600}
.nav-line{position:absolute;left:778px;top:0;width:1px;height:30px;background:var(--coal)}

/* hero */
.hero{left:0;top:82px;width:1200px;height:518px;background:radial-gradient(ellipse at 50% 45%,#5a5a5a 0%,#3a3a3a 45%,#1e1e1e 100%)}
.hero .brand{position:absolute;left:365px;top:222px;font-size:56px;color:var(--white);gap:16px;letter-spacing:2px}
.hero .brand-mark{width:44px;height:44px}
.hero .brand-sub{left:646px;top:291px;font-size:12px;color:var(--silver)}
.scroll-cue{position:absolute;left:591px;top:457px}

/* about */
.about-photo{left:575px;top:713px;width:390px;height:337px;background:linear-gradient(135deg,#2a2a2a,#6a6a6a 55%,#1a1a1a);box-shadow:0 8px 24px rgba(0,0,0,.18)}
.about-card{left:237px;top:675px;width:389px;min-height:338px;background:var(--white);box-shadow:0 6px 30px rgba(0,0,0,.12);padding:20px 30px 24px}
.section-title{font-family:var(--serif);font-weight:400;letter-spacing:4px;text-transform:uppercase;color:var(--black)}
.about-card .section-title{font-size:28px;line-height:38px}
.about-lead{margin-top:12px;font-size:11.8px;font-weight:500;line-height:21px;color:var(--coal);letter-spacing:-.1px}
.about-body{margin-top:12px;font-size:10.8px;line-height:21px;color:var(--ash);letter-spacing:-.1px}
.about-body+.about-body{margin-top:12px}
.text-link{display:inline-flex;align-items:center;gap:6px;font-size:10.5px;font-weight:600;letter-spacing:.4px;color:var(--coal);text-transform:uppercase;text-decoration:none;white-space:nowrap}
.about-card .text-link{margin-top:12px}

/* work */
.work{left:0;top:1125px;width:1200px;height:658px;background:var(--paper)}
.work .section-title{position:absolute;top:68px;width:1200px;text-align:center;font-size:28px}
.project-grid{position:absolute;left:162px;top:137px;width:876px;display:grid;grid-template-columns:repeat(3,292px)}
.project{height:194px;background:var(--white)}
.project-title{height:37px;padding:11px 15px;font-size:12px;font-weight:500;color:var(--coal);border:1px solid var(--mist)}
.project-photo{position:relative;height:157px}
.project.is-active .project-title{background:var(--coal);color:var(--white);border-color:var(--coal)}
.project.is-active .project-photo::after{content:"";position:absolute;inset:0;background:rgba(120,120,120,.55)}
.plus{position:absolute;left:131px;top:64px;z-index:1}
.tone-a{background:linear-gradient(160deg,#555,#2b2b2b)}
.tone-b{background:radial-gradient(ellipse at 50% 55%,#d8d8d8 0%,#6e6e6e 25%,#262626 70%)}
.tone-c{background:linear-gradient(135deg,#9a9a9a,#3d3d3d 60%,#1d1d1d)}
.tone-d{background:linear-gradient(120deg,#1b1b1b,#4a4a4a 50%,#202020)}
.tone-e{background:radial-gradient(ellipse at 40% 40%,#8a8a8a,#1e1e1e 75%)}
.tone-f{background:linear-gradient(110deg,#2a2a2a,#bdbdbd 45%,#2e2e2e 80%)}
.work .text-link{position:absolute;top:573px;left:538px;font-size:9.5px}

/* contact */
.contact-title{left:0;top:1850px;width:1200px;text-align:center;font-size:28px}
.contact-box{left:237px;top:1928px;width:728px;height:319px;border:1px solid var(--mist);box-shadow:0 6px 30px rgba(0,0,0,.05);display:flex}
.contact-info{width:361px;background:var(--white);padding:33px 58px 0;position:relative}
.contact-info h3{font-family:var(--serif);font-weight:400;font-size:17px;letter-spacing:3px;text-transform:uppercase;color:var(--black)}
.info-row{display:flex;align-items:center;gap:12px;width:236px;padding:12px 0;border-bottom:1px solid var(--mist);font-size:9.5px;line-height:15px;color:var(--ash)}
.info-row:first-of-type{margin-top:18px}
.info-icon{flex:0 0 30px;width:30px;height:30px;border-radius:50%;background:var(--coal);display:flex;align-items:center;justify-content:center}
.social{display:flex;align-items:center;gap:14px;margin-top:18px;font-size:10px;font-weight:600;color:var(--coal)}
.social-dot{width:13px;height:13px;border-radius:50%;background:var(--slate)}
.contact-form{flex:1;background:var(--paper);padding:37px 38px 0 38px}
.field{display:block;width:289px;height:28px;margin-bottom:13px;background:var(--white);border:1px solid var(--mist);padding:7px 10px;font-family:var(--sans);font-size:9.5px;color:var(--ash)}
.field.message{height:76px;margin-bottom:17px}
.submit{display:block;width:289px;height:30px;border-radius:15px;background:var(--slate);border:1px solid var(--coal);color:var(--white);font-family:var(--sans);font-size:10px;font-weight:700;letter-spacing:1.5px;text-align:center;line-height:28px}

/* footer */
.site-footer{left:0;top:2308px;width:1200px;height:249px;background:var(--coal);color:var(--ash)}
.site-footer .brand{position:absolute;left:488px;top:56px;font-size:28px;color:var(--white)}
.site-footer .brand-sub{left:588px;top:92px;color:var(--slate)}
.footer-nav{position:absolute;top:127px;left:0;width:1200px;font-size:10px;text-transform:uppercase;letter-spacing:.4px}
.footer-nav a{position:absolute;color:var(--ash);text-decoration:none}
.footer-nav .active{color:var(--white)}
.copyright{position:absolute;top:180px;width:1200px;text-align:center;font-size:10px;color:var(--slate)}
.copyright strong{color:var(--white);font-weight:500}
</style>
</head>
<body>

<header class="site-header abs">
  <div class="brand"><span class="brand-mark"></span>MOTOR VAULT</div>
  <span class="brand-sub">PART OF THE BRANTLEY GROUP</span>
  <span class="nav-line"></span>
  <nav class="main-nav">
    <a class="active" style="left:762px">Home</a>
    <a style="left:826px">About</a>
    <a style="left:895px">Our Work</a>
    <a style="left:987px">Contact</a>
  </nav>
</header>

<section class="hero abs" role="img" aria-label="Black and white photograph of workers excavating an underground construction site">
  <div class="brand"><span class="brand-mark"></span>MOTOR VAULT</div>
  <span class="brand-sub">PART OF THE BRANTLEY GROUP</span>
  <svg class="scroll-cue" width="18" height="26" viewBox="0 0 18 26" aria-hidden="true">
    <rect x="1" y="1" width="16" height="24" rx="8" fill="none" stroke="#e8e8e8" stroke-width="1.5"/>
    <line x1="9" y1="6" x2="9" y2="11" stroke="#e8e8e8" stroke-width="1.5"/>
  </svg>
</section>

<div class="about-photo abs" role="img" aria-label="Black and white photograph of a welder cutting steel with sparks flying"></div>
<article class="about-card abs">
  <h2 class="section-title">About Us</h2>
  <p class="about-lead">Designs and builds unique subterranean car parks for private residential homes in London and the influential counties within the UK</p>
  <p class="about-body">Lorem ipsum dolor sit amet, consectetur adipiscing elit, sed do eiusmod tempor incididunt ut labore et dolore magna aliqua. Ut enim ad minim veniam, quis nostrud exercitation ullamco laboris nisi ut aliquip ex ea commodo consequat.</p>
  <p class="about-body">Duis aute irure dolor in reprehenderit in voluptate velit esse cillum dolore eu fugiat nulla pariatur.</p>
  <a class="text-link">Know more about us
    <svg width="12" height="8" viewBox="0 0 12 8" aria-hidden="true"><path d="M0 4h10M7 1l3 3-3 3" fill="none" stroke="#1b1b1b" stroke-width="1.2"/></svg>
  </a>
</article>

<section class="work abs">
  <h2 class="section-title">Our Work</h2>
  <div class="project-grid">
    <div class="project is-active">
      <div class="project-title">Project Title Here</div>
      <div class="project-photo tone-a" role="img" aria-label="Underground site with timber props">
        <svg class="plus" width="30" height="30" viewBox="0 0 30 30" aria-hidden="true"><path d="M15 0v30M0 15h30" stroke="#fff" stroke-width="1.5"/></svg>
      </div>
    </div>
    <div class="project">
      <div class="project-title">Project Title Here</div>
      <div class="project-photo tone-b" role="img" aria-label="Concrete tunnel of a finished underground car park"></div>
    </div>
    <div class="project">
      <div class="project-title">Project Title Here</div>
      <div class="project-photo tone-c" role="img" aria-label="Steel beam framework viewed from below"></div>
    </div>
    <div class="project">
      <div class="project-title">Project Title Here</div>
      <div class="project-photo tone-d" role="img" aria-label="Lit underground passage with ceiling joists"></div>
    </div>
    <div class="project">
      <div class="project-title">Project Title Here</div>
      <div class="project-photo tone-e" role="img" aria-label="Dim excavation with work lights"></div>
    </div>
    <div class="project">
      <div class="project-title">Project Title Here</div>
      <div class="project-photo tone-f" role="img" aria-label="Light beam falling into a construction shaft"></div>
    </div>
  </div>
  <a class="text-link">View all projects
    <svg width="12" height="8" viewBox="0 0 12 8" aria-hidden="true"><path d="M0 4h10M7 1l3 3-3 3" fill="none" stroke="#1b1b1b" stroke-width="1.2"/></svg>
  </a>
</section>

<h2 class="section-title contact-title abs">Contact Us</h2>
<section class="contact-box abs">
  <div class="contact-info">
    <h3>Address</h3>
    <div class="info-row">
      <span class="info-icon"><svg width="14" height="14" viewBox="0 0 14 14" aria-hidden="true"><path d="M7 13S2.5 8 2.5 5.2a4.5 4.5 0 0 1 9 0C11.5 8 7 13 7 13z" fill="none" stroke="#fff" stroke-width="1.2"/><circle cx="7" cy="5.3" r="1.6" fill="none" stroke="#fff" stroke-width="1.2"/></svg></span>
      <span>42 Harrow Yard, London, W9 4KD |<br>Tel: 0207 555 0142</span>
    </div>
    <div class="info-row">
      <span class="info-icon"><svg width="14" height="14" viewBox="0 0 14 14" aria-hidden="true"><path d="M3 1.5l2.2 2.6-1.3 1.6c.9 1.8 2.3 3.2 4.2 4.2l1.6-1.3 2.6 2.2-1.4 1.7C6.6 12.3 1.9 7.6 1.3 3z" fill="none" stroke="#fff" stroke-width="1.2"/></svg></span>
      <span>020-555-0199</span>
    </div>
    <div class="info-row">
      <span class="info-icon"><svg width="14" height="14" viewBox="0 0 14 14" aria-hidden="true"><rect x="1.5" y="3" width="11" height="8" fill="none" stroke="#fff" stroke-width="1.2"/><path d="M1.5 3l5.5 4.5L12.5 3" fill="none" stroke="#fff" stroke-width="1.2"/></svg></span>
      <span>contactus@motorvault.example</span>
    </div>
    <div class="social">Connect With Us:
      <span class="social-dot" aria-label="Social profile"></span>
      <span class="social-dot" aria-label="Social profile"></span>
      <span class="social-dot" aria-label="Social profile"></span>
      <span class="social-dot" aria-label="Social profile"></span>
    </div>
  </div>
  <form class="contact-form">
    <span class="field">Your Name</span>
    <span class="field">Your Email</span>
    <span class="field">Phone</span>
    <span class="field message">Message</span>
    <span class="submit">SUBMIT</span>
  </form>
</section>

<footer class="site-footer abs">
  <div class="brand"><span class="brand-mark"></span>MOTOR VAULT</div>
  <span class="brand-sub">PART OF THE BRANTLEY GROUP</span>
  <nav class="footer-nav">
    <a class="active" style="left:471px">Home</a>
    <a style="left:530px">About</a>
    <a style="left:594px">Our Work</a>
    <a style="left:680px">Contact</a>
  </nav>
  <p class="copyright">Copyright © <strong>Motor Vault</strong> 2019. Terms and Conditions | Privacy Policy | Design By Northline Studio</p>
</footer>

</body>
</html>
```